Professional business cards for real estate development company

I need business cards for my new real estate development company. The company, "LUMAR" is a real estate development, investment, and advisory firm with a focus on multifamily, office, and mixed-use projects across primary and secondary markets in the Southeast United States.

Style preference is modern

Industry/Entity Type

Real Estate Development

Contact Information for Business Card

The business cards need to include:
Name
Title
Mailing Address
Phone Number
Web Address

Logo is attached. I would like white to be the primary color with incorporation of the company colors: #232D3A and #B5A451

Font styles to use
Other font styles liked:
• Montserrat, Avenir

Requirements
Must have
• Company Logo. No need to include the company name since the name is in the logo.
Should not have
• No line type designs

```html
<!DOCTYPE html>
<html lang="en">
<head>
<meta charset="utf-8">
<title>LUMAR Business Card</title>
<link href="https://fonts.googleapis.com/css2?family=Roboto:wght@300;400;500&display=swap" rel="stylesheet">
<style>
  :root {
    --backdrop: #2b2b2b;
    --navy: #202633;
    --navy-deep: #141921;
    --paper: #efefef;
    --ink: #2a2f3a;
    --white: #ffffff;
  }
  html, body {
    margin: 0;
    padding: 0;
    width: 1200px;
    height: 1138px;
    overflow: hidden;
    background: var(--backdrop);
    font-family: "Roboto", Arial, sans-serif;
  }
  .card {
    position: absolute;
    width: 621px;
    height: 374px;
    border-radius: 16px;
    overflow: hidden;
  }
  .card-front {
    left: 275px;
    top: 186px;
    background: var(--navy);
  }
  .card-back {
    left: 276px;
    top: 608px;
    background: var(--paper);
  }
  .wordmark {
    position: absolute;
    margin: 0;
    font-weight: 500;
    font-size: 52px;
    letter-spacing: 2px;
    line-height: 1;
  }
  .card-front .wordmark {
    left: 0;
    right: 0;
    top: 198px;
    text-align: center;
    color: var(--navy-deep);
  }
  .card-back .wordmark {
    left: 57px;
    top: 190px;
    color: var(--navy);
  }
  .wave {
    position: absolute;
    left: 0;
    top: 0;
    width: 621px;
    height: 374px;
  }
  .person {
    position: absolute;
    right: 38px;
    top: 24px;
    text-align: right;
    color: var(--white);
  }
  .person-name {
    margin: 0;
    font-size: 24px;
    font-weight: 400;
    line-height: 1.2;
  }
  .person-title {
    margin: 2px 0 0;
    font-size: 15px;
    font-weight: 300;
  }
  .address {
    position: absolute;
    left: 39px;
    top: 294px;
    margin: 0;
    font-size: 15px;
    font-weight: 300;
    line-height: 24px;
    color: var(--ink);
    font-style: normal;
  }
  .contacts {
    position: absolute;
    right: 38px;
    top: 272px;
    margin: 0;
    padding: 0;
    list-style: none;
    font-size: 15px;
    font-weight: 300;
    color: var(--ink);
  }
  .contacts li {
    display: flex;
    justify-content: flex-end;
    align-items: center;
    height: 24px;
  }
  .contacts svg {
    width: 14px;
    height: 14px;
    margin-left: 16px;
    fill: var(--navy);
  }
</style>
</head>
<body>
  <section class="card card-front">
    <h1 class="wordmark">LUMAR</h1>
  </section>

  <section class="card card-back">
    <svg class="wave" viewBox="0 0 776 468" preserveAspectRatio="none" aria-hidden="true">
      <path class="wave-band" d="M0,0 H776 V162 C750,175 720,190 660,188 C580,182 500,125 400,76 C300,48 150,48 0,72 Z" fill="#202633"/>
      <path class="wave-stripe-top" d="M0,56 C120,10 300,12 440,68 C300,28 120,24 0,66 Z" fill="#ffffff"/>
      <path class="wave-stripe-low" d="M400,76 C500,120 580,170 660,168 C720,166 750,152 776,140 L776,150 C750,162 720,176 660,178 C570,180 500,130 400,76 Z" fill="#efefef"/>
    </svg>

    <div class="person">
      <p class="person-name">John Doe Smith</p>
      <p class="person-title">Managing Director</p>
    </div>

    <h2 class="wordmark">LUMAR</h2>

    <address class="address">234 Anywhere St., Any City,<br>Any Town, US 123456</address>

    <ul class="contacts">
      <li>828-111-1111
        <svg viewBox="0 0 16 16"><path d="M2 6c0-2 2-3 6-3s6 1 6 3v1h-3V5.5H5V7H2z M4 8h8l1 5H3z"/></svg>
      </li>
      <li>john@yourwebsite.com
        <svg viewBox="0 0 16 16"><path d="M1 3h14v10H1z M2 4l6 5 6-5" fill="none" stroke="#202633" stroke-width="1.6"/></svg>
      </li>
      <li>www.yourwebsite.com
        <svg viewBox="0 0 16 16"><circle cx="8" cy="8" r="6.5" fill="none" stroke="#202633" stroke-width="1.3"/><path d="M1.5 8h13 M8 1.5v13 M8 1.5c-3 3-3 10 0 13 M8 1.5c3 3 3 10 0 13" fill="none" stroke="#202633" stroke-width="1"/></svg>
      </li>
    </ul>
  </section>
</body>
</html>
```